Two sided flyer design with a cut out discount coupon

We are an established tech repair company in Greece and we need an A5, two sided flyer design with a cut out discount coupon.

The final design should pinpoint our services/customer benefits, highlight mainly the city locations and drive target audience to visit one of our stores and make use of the discount coupon.

We would like to see designs that use only the colors Orange/black/grey/white. Check and follow the look and feel of our website www.fixorbit.gr

We would like to keep the idea of the map with pins to all locations, we don't mind if it is in a smaller scale. (see old flyer)

Find attached company photos you can use, our logo and a sample of our old flyer.

Use the text info below:

1.who we are -what we do
SMARTPHONE TABLETS LAPTOPS PC REPAIRS | ACCESSORIES FOR SMARTPHONES AND TABLETS

3. ΒΕΝΕFITS
Repairs in 20 minutes
Low Price Guarantee
6 Interest Free payments
Open view service
Motherboard Repairs

2. We need to show that we have 25 stores nationwide but focus mainly on the 8 city locations. We need to put the location of the store, address and phone number.

GLYFADA address: Ther. Latsou 54 Phone: 2104738215

MAROUSI address:----------------------------- Phone:-----------------------

PERISTERI :----------------------------- Phone:-----------------------

NEA ERYTHRAIA:----------------------------- Phone:-----------------------

AMFITHEAS :----------------------------- Phone:-----------------------

AGIA PARASKEYI :----------------------------- Phone:-----------------------

SYNTAGMA:----------------------------- Phone:-----------------------

PEIRAIAS:----------------------------- Phone:-----------------------

3. CUT OUT DISCOUNT COUPON

Come to an Fixorbit store with this coupon and claim 10% discount on repairs and 15% on gadgets and accessories

*Valid until:…..

5. Contact info

www.Fixorbit.gr plain unlettered badge icon /FixorbitHellas Twitter icon/@FixorbitHellas Insta icon/ @Fixorbit_gr

Please contact us for any information/clarification you may need.

Thank you

```html
<!DOCTYPE html>
<html lang="en">
<head>
<meta charset="utf-8">
<title>Fixorbit – A5 two sided flyer</title>
<link href="https://fonts.googleapis.com/css2?family=Didact+Gothic&family=Audiowide&display=swap" rel="stylesheet">
<style>
  :root{
    --orange:#f28c1b;
    --black:#0d0d0d;
    --charcoal:#2b2b2b;
    --grey:#cfcfcf;
    --grey-light:#ececec;
    --white:#ffffff;
    --stage:#e6e5e3;
    --body:"Didact Gothic", sans-serif;
    --display:"Audiowide", sans-serif;
  }
  *{box-sizing:border-box;margin:0;padding:0}
  html,body{width:1200px;height:849px;overflow:hidden;background:var(--stage);font-family:var(--body)}
  .canvas{position:relative;width:1200px;height:849px}
  .page{position:absolute;top:64px;width:509px;height:720px;overflow:hidden;box-shadow:0 10px 24px rgba(0,0,0,.18)}
  .page--front{left:51px;background:var(--black)}
  .page--back{left:640px;background:var(--white)}
  .abs{position:absolute}
  .photo{position:absolute;background:linear-gradient(160deg,#6f6f6f 0%,#3a3a3a 55%,#1c1c1c 100%)}
  .photo--light{background:linear-gradient(170deg,#d9d9d9 0%,#8d8d8d 45%,#3b3b3b 100%)}

  /* front */
  .front-header{left:0;top:0;width:509px;height:100px;background:var(--charcoal)}
  .brand{display:flex;align-items:center;gap:8px;color:var(--white);font-size:34px;line-height:1}
  .brand__square{width:24px;height:24px;background:var(--orange);border-radius:3px}
  .front-header .brand{position:absolute;left:22px;top:30px}
  .front-header__band{position:absolute;right:0;top:0}
  .front-header__url{position:absolute;right:26px;top:54px;font-size:22px;color:var(--black)}
  .benefits{left:148px;top:272px;width:214px;text-align:center;color:var(--white);font-size:15.5px;line-height:1.55}
  .repairs-band{left:0;top:400px;width:509px;height:68px;background:var(--orange);display:flex;align-items:center;justify-content:center}
  .repairs-band__word{font-family:var(--display);font-size:60px;letter-spacing:10px;color:var(--black);line-height:1}
  .accessories{left:0;top:478px;width:509px;text-align:center;color:var(--orange);font-size:13px;letter-spacing:1.6px}
  .categories{left:0;top:502px;width:509px;display:flex;justify-content:space-around;color:var(--white);font-size:13px;letter-spacing:1.5px}
  .device-area{left:0;top:524px;width:509px;height:138px;background:var(--orange)}
  .device-area svg{position:absolute;left:0;top:0}
  .device{position:absolute;top:18px;width:104px;height:104px;border-radius:50%;border:4px solid var(--black);background:linear-gradient(150deg,#bfc7cf 0%,#5d6b78 60%,#2a2f35 100%)}
  .partners{left:0;top:662px;width:509px;height:58px;background:var(--white);display:flex;align-items:center;justify-content:space-evenly;padding:0 10px}
  .partner{width:40px;height:12px;background:var(--grey);border-radius:2px}

  /* back */
  .map-area{left:0;top:0;width:392px;height:300px;background:radial-gradient(ellipse 62% 58% at 44% 52%,#ffffff 0%,#f4f4f4 45%,var(--grey) 100%)}
  .map-pins{position:absolute;left:0;top:0}
  .store-column{left:400px;top:0;width:109px;height:720px;background:var(--black);border-left:8px solid var(--orange)}
  .stores{position:absolute;right:10px;top:40px;width:150px;text-align:right;list-style:none}
  .store{margin-bottom:17px;color:var(--white);line-height:1.25}
  .store__name{font-size:11px;letter-spacing:.4px}
  .store__addr{font-size:8.5px;color:#d8d8d8}
  .store__phone{font-size:8.5px;display:flex;justify-content:flex-end;align-items:center;gap:4px}
  .store__phone::before{content:"";width:7px;height:7px;background:var(--orange);display:inline-block}
  .store-column .brand{position:absolute;left:8px;bottom:38px;font-size:20px;gap:5px}
  .store-column .brand__square{width:14px;height:14px}
  .coupon{left:14px;top:562px;width:366px;height:84px;border:2px dashed var(--black);padding:6px 12px;font-size:10.5px;color:#222}
  .coupon__line{display:block;line-height:24px;white-space:nowrap}
  .coupon__line--small{line-height:16px;font-size:9.5px}
  .coupon__big{font-size:20px;font-weight:700;font-style:italic;color:var(--black);margin:0 4px}
  .social-badge{left:14px;top:656px;width:66px;height:14px;background:#4a5f8f;border-radius:7px}
  .fineprint{left:14px;top:680px;font-size:8px;color:#444;white-space:nowrap}
</style>
</head>
<body>
<main class="canvas">

  <!-- Front side -->
  <section class="page page--front" aria-label="Flyer front">
    <header class="abs front-header">
      <div class="brand"><span class="brand__square"></span>Fixorbit</div>
      <svg class="front-header__band" width="260" height="100" viewBox="0 0 260 100" aria-hidden="true">
        <polygon points="40,0 260,0 260,100 0,100" fill="var(--orange)"/>
        <polygon points="40,0 60,0 20,100 0,100" fill="#1a1a1a" opacity=".35"/>
      </svg>
      <span class="front-header__url">www.fixorbit.gr</span>
    </header>

    <div class="photo" style="left:0;top:100px;width:509px;height:158px" role="img" aria-label="Store interior with technicians at repair benches"></div>

    <div class="photo" style="left:14px;top:270px;width:126px;height:122px" role="img" aria-label="Customer at the service counter"></div>
    <p class="abs benefits">Repairs in 20 minutes<br>Low Price Guarantee<br>6 Interest Free payments<br>Open view service<br>Motherboard Repairs</p>
    <div class="photo" style="left:370px;top:270px;width:125px;height:122px" role="img" aria-label="Accessories shelves inside the store"></div>

    <div class="abs repairs-band"><span class="repairs-band__word">repairs</span></div>
    <p class="abs accessories">ACCESSORIES FOR SMARTPHONES AND TABLETS</p>
    <div class="abs categories"><span>SMARTPHONE</span><span>TABLETS</span><span>LAPTOPS</span><span>PC</span></div>

    <div class="abs device-area">
      <svg width="509" height="138" viewBox="0 0 509 138" aria-hidden="true">
        <polygon points="0,0 509,0 509,20 0,60" fill="var(--black)"/>
      </svg>
      <div class="device" style="left:14px" role="img" aria-label="Smartphone"></div>
      <div class="device" style="left:136px" role="img" aria-label="Tablets"></div>
      <div class="device" style="left:262px" role="img" aria-label="Laptop"></div>
      <div class="device" style="left:388px" role="img" aria-label="Desktop PC"></div>
    </div>

    <div class="abs partners" aria-label="Supported device makers">
      <span class="partner"></span><span class="partner"></span><span class="partner"></span>
      <span class="partner"></span><span class="partner"></span><span class="partner"></span>
      <span class="partner"></span><span class="partner"></span><span class="partner"></span>
    </div>
  </section>

  <!-- Back side -->
  <section class="page page--back" aria-label="Flyer back">
    <div class="abs map-area" role="img" aria-label="Map of Greece with pins marking all 25 store locations, from Thessaloniki down to Athens, the islands and Crete">
      <svg class="map-pins" width="392" height="300" viewBox="0 0 392 300" aria-hidden="true">
        <defs>
          <g id="pin">
            <path d="M0 -20a7 7 0 0 1 7 7c0 5-7 13-7 13s-7-8-7-13a7 7 0 0 1 7-7z" fill="var(--black)"/>
            <circle cx="0" cy="-13" r="3" fill="var(--orange)"/>
          </g>
        </defs>
        <use href="#pin" x="172" y="40"/>
        <use href="#pin" x="104" y="58"/>
        <use href="#pin" x="76" y="80"/>
        <use href="#pin" x="112" y="78"/>
        <use href="#pin" x="108" y="108"/>
        <use href="#pin" x="134" y="118"/>
        <use href="#pin" x="120" y="128"/>
        <use href="#pin" x="78" y="138"/>
        <use href="#pin" x="86" y="168"/>
        <use href="#pin" x="150" y="146"/>
        <use href="#pin" x="154" y="184"/>
        <use href="#pin" x="196" y="196"/>
        <use href="#pin" x="124" y="228"/>
        <use href="#pin" x="146" y="236"/>
      </svg>
    </div>

    <div class="photo photo--light" style="left:8px;top:308px;width:380px;height:245px" role="img" aria-label="Wide view of the repair workshop"></div>

    <p class="abs coupon">
      <span class="coupon__line">Come to an Fixorbit store with this coupon and claim <span class="coupon__big">10%</span></span>
      <span class="coupon__line">discount on repairs and <span class="coupon__big">15%</span> on gadgets and accessories</span>
      <span class="coupon__line coupon__line--small">*Valid until ........................</span>
    </p>

    <span class="abs social-badge" aria-hidden="true"></span>
    <p class="abs fineprint">www.Fixorbit.gr &nbsp;/FixorbitHellas &nbsp;@FixorbitHellas &nbsp;@Fixorbit_gr</p>

    <aside class="abs store-column">
      <ul class="stores">
        <li class="store"><div class="store__name">GLYFADA</div><div class="store__addr">Ther. Latsou 54</div><div class="store__phone">2104738215</div></li>
        <li class="store"><div class="store__name">MAROUSI</div><div class="store__addr">12, Anemonis Street</div><div class="store__phone">210 634 1187</div></li>
        <li class="store"><div class="store__name">PERISTERI</div><div class="store__addr">Kyprou Street 19</div><div class="store__phone">210 5723 914</div></li>
        <li class="store"><div class="store__name">NEA ERYTHRAIA</div><div class="store__addr">Dafnis Street 8</div><div class="store__phone">210 8047 326</div></li>
        <li class="store"><div class="store__name">AMFITHEAS</div><div class="store__addr">Orfeos Street 27</div><div class="store__phone">216 7013 452</div></li>
        <li class="store"><div class="store__name">AGIA PARASKEYI</div><div class="store__addr">112 Lilaion Ave.</div><div class="store__phone">216 7013 468</div></li>
        <li class="store"><div class="store__name">SYNTAGMA</div><div class="store__addr">0000000000</div><div class="store__phone">216 7013 468</div></li>
        <li class="store"><div class="store__name">PEIRAIAS</div><div class="store__addr">0000000000</div><div class="store__phone">216 7013 468</div></li>
      </ul>
      <div class="brand"><span class="brand__square"></span>Fixorbit</div>
    </aside>
  </section>

</main>
</body>
</html>
```